Riverstone & Pine Construction and Developments business cards

A business card with watermark background (construction work)

Company logo attached

Home improvement projects
House renovations
Bathroom and kitchen renovations
House extensions
New builds and granny flats

Director Omar Haddine
(Phone number)
omar@rpcbuildgroup.com.au
(Instagram logo) rpc_buildgroup

```html
<!DOCTYPE html>
<html lang="en">
<head>
<meta charset="utf-8">
<title>Riverstone &amp; Pine – Business Cards</title>
<link href="https://fonts.googleapis.com/css2?family=Bebas+Neue&family=Montserrat:wght@400;500&family=Roboto:wght@400&display=swap" rel="stylesheet">
<style>
  :root {
    --backdrop: #3b3b3d;
    --brand-blue: #3277b6;
    --card-white: #ffffff;
    --ink-dark: #3a3a3a;
  }
  * { margin: 0; padding: 0; box-sizing: border-box; }
  html, body { width: 1200px; height: 1200px; overflow: hidden; }
  body { background: var(--backdrop); position: relative; font-family: "Montserrat", sans-serif; }

  .panel { position: absolute; }
  .panel--blue { background: var(--brand-blue); color: var(--card-white); }
  .panel--white { background: var(--card-white); }

  /* Front card */
  .front-contact { left: 262px; top: 165px; width: 328px; height: 392px; }
  .front-brand { left: 596px; top: 165px; width: 352px; height: 392px; }
  /* Back card */
  .back-brand { left: 262px; top: 653px; width: 336px; height: 392px; }
  .back-services { left: 605px; top: 653px; width: 343px; height: 392px; }

  .contact-block { position: absolute; left: 35px; top: 123px; }
  .person-name {
    font-family: "Bebas Neue", sans-serif;
    font-size: 31px; line-height: 1; letter-spacing: 0.3px;
  }
  .person-role { font-size: 15.5px; margin-top: 4px; }
  .contact-list { list-style: none; margin-top: 17px; }
  .contact-list li {
    display: flex; align-items: center; gap: 9px;
    font-size: 15.5px; line-height: 20px;
  }
  .contact-list svg { width: 13px; height: 13px; flex: none; fill: var(--card-white); }

  .wordmark {
    position: absolute; left: 0; right: 0; top: 50%;
    transform: translateY(-50%);
    display: flex; align-items: center; justify-content: center; gap: 10px;
    color: var(--brand-blue); font-weight: 500; text-align: center;
  }
  .wordmark__square { width: 14px; height: 14px; background: var(--brand-blue); flex: none; }
  .wordmark__name { font-size: 22px; line-height: 1.2; }
  .wordmark__name small { display: block; font-size: 12.5px; letter-spacing: 1px; }

  .service-list {
    list-style: none; position: absolute; right: 26px; top: 133px;
    font-family: "Roboto", sans-serif; font-size: 15.5px; text-align: right;
  }
  .service-list li {
    display: flex; align-items: center; justify-content: flex-end; gap: 10px;
    height: 25px;
  }
  .service-list svg { width: 9px; height: 9px; fill: var(--card-white); flex: none; }
</style>
</head>
<body>
  <section class="panel panel--blue front-contact">
    <div class="contact-block">
      <h1 class="person-name">OMAR HADDINE</h1>
      <p class="person-role">Director</p>
      <ul class="contact-list">
        <li><svg viewBox="0 0 16 16"><path d="M3.6 1.2l2.3 2.9-1.4 1.8c.9 2 2.6 3.7 4.6 4.6l1.8-1.4 2.9 2.3-1.2 2.6C6.8 13.6 2.4 9.2 1 3.4z"/></svg>369-555-0142</li>
        <li><svg viewBox="0 0 16 16"><path d="M1 3h14v10H1z M2 4.3v.3l6 4 6-4v-.3z" fill-rule="evenodd"/></svg>omar@rpcbuildgroup.com.au</li>
        <li><svg viewBox="0 0 16 16"><circle cx="8" cy="8" r="7"/><path d="M5 4c2 1 1 3 3 3s1 3 3 2" stroke="#3277b6" stroke-width="1.4" fill="none"/></svg>www.rpcbuildgroup.com.au</li>
        <li><svg viewBox="0 0 16 16"><circle cx="8" cy="8" r="7"/></svg>rpc_buildgroup</li>
      </ul>
    </div>
  </section>
  <section class="panel panel--white front-brand">
    <div class="wordmark">
      <span class="wordmark__square"></span>
      <p class="wordmark__name">Riverstone &amp; Pine<small>Construction and Developments</small></p>
    </div>
  </section>

  <section class="panel panel--white back-brand">
    <div class="wordmark">
      <span class="wordmark__square"></span>
      <p class="wordmark__name">Riverstone &amp; Pine<small>Construction and Developments</small></p>
    </div>
  </section>
  <section class="panel panel--blue back-services">
    <ul class="service-list">
      <li>Home improvement projects<svg viewBox="0 0 9 9"><rect width="4" height="4"/><rect x="5" width="4" height="4"/><rect y="5" width="4" height="4"/><rect x="5" y="5" width="4" height="4"/></svg></li>
      <li>House renovations<svg viewBox="0 0 9 9"><rect width="4" height="4"/><rect x="5" width="4" height="4"/><rect y="5" width="4" height="4"/><rect x="5" y="5" width="4" height="4"/></svg></li>
      <li>Bathroom &amp; kitchen renovations<svg viewBox="0 0 9 9"><rect width="4" height="4"/><rect x="5" width="4" height="4"/><rect y="5" width="4" height="4"/><rect x="5" y="5" width="4" height="4"/></svg></li>
      <li>House extensions<svg viewBox="0 0 9 9"><rect width="4" height="4"/><rect x="5" width="4" height="4"/><rect y="5" width="4" height="4"/><rect x="5" y="5" width="4" height="4"/></svg></li>
      <li>New builds &amp; granny flats<svg viewBox="0 0 9 9"><rect width="4" height="4"/><rect x="5" width="4" height="4"/><rect y="5" width="4" height="4"/><rect x="5" y="5" width="4" height="4"/></svg></li>
    </ul>
  </section>
</body>
</html>
```